Professionell und kommunikativ, kommen gerne wieder.
Zielgruppe
Wir transportieren Güter und Waren aller Art rund um die Welt. Hauptsächlich Luftfracht, aber auch per Schiff und an Land. Hauptsächlich richten wir uns damit an Firmenkunden, weniger an Privatkunden. Für unsere neue Website benötigen wir ein Design.
Aufgabenstellung
Wir benötigen ein Webdesign für den Relaunch unserer Website. Unsere Ideen für unsere neue Website haben wir bereits skizziert (Anlage). Diese Mockups bedürfen nun eines Designs.
Dazu ergänzend gelten die folgenden, formalen Vorgaben:
• 1140px breit, gerne auch Ideen für die Darstellung auf Smartphones und Tablets
• Logo links oben
• Navigation oben waagerecht
• Dropdown-Navigation am Desktop, Hamburger für die mobile Navigation
• Verwendung eines Grid-Systems wie Bootstrap
• Mindestschriftgröße für Mengentext: 16px (bei groß ausfallenden Fonts 15px)
Wir haben keine Hausschriftart und keine festgelegten Farben. Wir möchten aber unser Logo weiterverwenden und da bietet es sich natürlich an, auf dem Rot aufzubauen.

```html
<!DOCTYPE html>
<html lang="en">
<head>
<meta charset="utf-8">
<title>VeloCargo – Get a Quote</title>
<link href="https://fonts.googleapis.com/css2?family=Inter:wght@400;500;600;700&display=swap" rel="stylesheet">
<style>
:root{
  --red:#e2001a;
  --ink:#1d1d1f;
  --text:#444;
  --muted:#8a8a8a;
  --line:#dcdcdc;
  --soft:#f6f6f6;
  --navy:#1f3a4d;
  --footer:#2a2a2a;
  --white:#fff;
}
*{box-sizing:border-box;margin:0;padding:0}
html,body{width:1200px;height:4068px;overflow:hidden}
body{position:relative;font-family:"Inter",Arial,sans-serif;color:var(--ink);background:var(--white)}
.abs{position:absolute}
.eyebrow{position:absolute;font-size:9px;letter-spacing:.06em;text-transform:uppercase;color:var(--ink);display:flex;align-items:center;gap:14px}
.eyebrow::before{content:"";width:24px;height:2px;background:var(--red)}
.eyebrow span{color:var(--muted)}
.h2{position:absolute;font-size:33px;font-weight:700;letter-spacing:-.01em;color:var(--ink)}

/* top bar + header */
.topbar{position:absolute;left:0;top:0;width:1200px;height:19px;background:#fff;font-size:8px;letter-spacing:.06em;color:#555}
.topbar .l{position:absolute;left:186px;top:5px}
.topbar .r{position:absolute;left:787px;top:5px}
.header{position:absolute;left:0;top:19px;width:1200px;height:65px;background:#fff;border-top:1px solid #eee}
.brand{position:absolute;left:188px;top:21px;font-size:20px;font-weight:700;letter-spacing:-.02em;color:var(--ink);display:flex;align-items:center;gap:8px}
.brand i{display:block;width:14px;height:14px;background:var(--red)}
.nav{position:absolute;left:690px;top:33px;display:flex;gap:20px;font-size:9px;letter-spacing:.06em;color:#555;font-weight:500}
.nav-cta{position:absolute;left:911px;top:11px;width:101px;height:54px;background:var(--red);color:#fff;font-size:9px;font-weight:600;letter-spacing:.06em;display:flex;align-items:center;justify-content:center}

/* hero */
.hero{position:absolute;left:0;top:84px;width:1200px;height:469px;background:linear-gradient(100deg,#4a4a4a 0%,#6a6c6e 45%,#8a8c8e 100%)}
.hero h1{position:absolute;left:186px;top:178px;font-size:48px;line-height:1.1;font-weight:600;color:#fff}
.hero p{position:absolute;left:186px;top:290px;width:300px;font-size:11px;line-height:1.45;color:#eee}
.hero .btn{position:absolute;left:186px;top:387px;width:110px;height:40px;background:var(--red);color:#fff;font-size:9px;font-weight:600;letter-spacing:.06em;display:flex;align-items:center;justify-content:center}
.side-tabs{position:absolute;left:1143px;top:303px;width:57px}
.side-tabs div{height:54px;margin-bottom:4px;background:var(--red);color:#fff;font-size:7px;font-weight:600;text-align:center;padding-top:12px}
.side-tabs svg{display:block;margin:0 auto 4px}

/* about */
.about-text{position:absolute;left:186px;top:820px;width:420px;font-size:13px;line-height:1.4;color:var(--text)}
.about-small{position:absolute;left:186px;width:420px;font-size:10px;line-height:1.5;color:var(--muted)}
.btn-outline{position:absolute;border:2px solid var(--ink);font-size:9px;font-weight:600;letter-spacing:.14em;display:flex;align-items:center;justify-content:center}
.about-img{position:absolute;left:663px;top:712px;width:347px;height:291px;background:linear-gradient(160deg,#7a8794 0%,#a06b45 55%,#5b6670 100%)}

/* services */
.pager{position:absolute;left:800px;top:1176px;display:flex;align-items:center;gap:14px;font-size:11px;color:var(--muted)}
.pager .next{width:29px;height:29px;background:#333;display:flex;align-items:center;justify-content:center}
.card{position:absolute;top:1252px;width:225px;height:245px;background:var(--soft);padding:30px 34px 0;overflow:hidden}
.card .ic{position:relative;width:46px;height:46px;margin-bottom:26px}
.card .badge{position:absolute;left:30px;top:-6px;width:18px;height:18px;background:var(--red)}
.card h3{font-size:14px;font-weight:400;line-height:1.3;color:#555}
.card h3 b{font-weight:600;color:var(--ink)}
.card p{margin-top:8px;font-size:9px;line-height:1.5;color:var(--muted)}

/* reach out */
.reach{position:absolute;left:0;top:1623px;width:1200px;height:393px;background:var(--navy)}
.reach-img{position:absolute;left:663px;top:0;width:537px;height:393px;background:linear-gradient(135deg,#4d6473 0%,#7a5845 50%,#2f4350 100%)}
.reach h2{position:absolute;left:186px;top:76px;font-size:36px;font-weight:700;color:#fff}
.reach p{position:absolute;left:186px;top:124px;width:420px;font-size:17px;line-height:1.25;font-weight:500;color:#dfe6ea}
.reach .btn-outline{left:186px;top:204px;width:165px;height:44px;border-color:#fff;color:#fff}
.reach .phone{position:absolute;left:382px;top:214px;display:flex;align-items:center;gap:10px;font-size:18px;color:#fff}
.reach .hours{position:absolute;left:186px;top:293px;display:flex;gap:24px;font-size:9px;color:#b9c5cd}
.reach .hours b{display:block;color:#fff;font-weight:500}

/* philosophy */
.center{left:0;width:1200px;justify-content:center;text-align:center}
.pcard{position:absolute;background:var(--soft);padding:28px 26px 0}
.pcard h3{margin-top:14px;font-size:14px;font-weight:600;color:#444}
.pcard p{margin-top:10px;font-size:9px;line-height:1.55;color:var(--muted)}

/* faq */
.faq{position:absolute;height:52px;background:var(--soft);padding:0 44px 0 20px;display:flex;align-items:center;font-size:12px;font-weight:600;line-height:1.35;color:#444}
.faq::after{content:"+";position:absolute;right:24px;top:50%;transform:translateY(-50%);font-size:15px;font-weight:400;color:#555}

/* partners */
.partner{position:absolute;top:3392px;display:flex;align-items:center;gap:8px;font-size:20px;color:#333}
.partner i{display:block;width:22px;height:22px;border:2px solid #333;border-radius:50%}

/* footer */
.footer{position:absolute;left:0;top:3562px;width:1200px;height:506px;background:var(--footer);color:#9a9a9a}
.footer .logo{position:absolute;left:186px;top:82px;font-size:19px;font-weight:700;letter-spacing:-.02em;color:#bbb;display:flex;align-items:center;gap:8px}
.footer .logo i{display:block;width:12px;height:12px;background:var(--red)}
.footer .tag{position:absolute;left:186px;top:120px;font-size:9px;line-height:1.6;font-weight:600;color:#9a9a9a}
.footer .cert{position:absolute;left:186px;top:196px;width:76px;height:48px;border-radius:4px;background:#5a5a5a}
.footer .cert-t{position:absolute;left:186px;top:257px;font-size:9px;font-weight:600}
.fcol{position:absolute;font-size:9px;line-height:1}
.fcol h4{font-size:9px;font-weight:600;letter-spacing:.14em;color:#8a8a8a;margin-bottom:22px}
.fcol a{display:block;color:#7a7a7a;text-decoration:none;font-size:8px;letter-spacing:.04em;margin:0 0 20px 14px}
.footer .rule{position:absolute;left:398px;top:291px;width:296px;height:1px;background:#444}
.footer .map{position:absolute;left:750px;top:81px;width:262px;height:161px;background:linear-gradient(135deg,#d7dde2,#b9c8d4)}
.footer .rating{position:absolute;left:186px;top:351px;width:217px;height:74px;border-radius:4px;background:#e8e8e8}
.footer .contact{position:absolute;left:750px;top:264px;font-size:8px;line-height:1.75;color:#7d7d7d}
.footer .contact h4{font-size:9px;font-weight:600;letter-spacing:.14em;color:#8a8a8a;margin-bottom:18px}
.footer .contact b{color:#9a9a9a;font-weight:600}
.footer .btn-outline{left:750px;top:393px;width:262px;height:32px;border:1px solid #888;color:#999;font-size:9px}

/* overlay + modal */
.overlay{position:absolute;left:0;top:0;width:1200px;height:4068px;background:rgba(0,0,0,.56)}
.modal{position:absolute;left:268px;top:134px;width:664px;height:984px;background:#fff}
.modal .close{position:absolute;left:628px;top:20px}
.modal .eyebrow{left:35px;top:34px;font-size:9px}
.modal h2{position:absolute;left:35px;top:56px;font-size:34px;font-weight:600;letter-spacing:-.01em}
.modal .intro{position:absolute;left:35px;top:116px;width:590px;font-size:12.5px;line-height:1.6;color:#555}
.person{position:absolute;left:35px;top:177px;display:flex;align-items:center;gap:12px}
.avatar{width:40px;height:40px;border-radius:50%;background:linear-gradient(180deg,#c9ccd0,#3f6d91)}
.person b{display:block;font-size:11px;font-weight:600}
.person span{font-size:11px;color:#555}
.group{position:absolute;left:35px;font-size:15px;font-weight:600}
.label{position:absolute;font-size:9.5px;font-weight:600}
.field{position:absolute;height:33px;border:1px solid var(--line);font-size:9.5px;color:#555;padding:0 10px;display:flex;align-items:center}
.field.ph{color:#9a9a9a}
.field .chev{position:absolute;right:12px;top:12px}
.area{height:123px;align-items:flex-start;padding-top:10px}
.consent{position:absolute;left:35px;top:856px;display:flex;gap:9px;font-size:10px;line-height:1.45;color:#444;width:470px}
.consent i{flex:none;display:block;width:10px;height:10px;border:1px solid #bbb;margin-top:1px}
.consent a{color:var(--red);text-decoration:none}
.submit{position:absolute;left:35px;top:911px;width:101px;height:38px;background:var(--red);color:#fff;font-size:10px;font-weight:700;display:flex;align-items:center;justify-content:center}
</style>
</head>
<body>

<div class="topbar"><span class="l">+49 61000 55512 • CALL US ANYTIME</span><span class="r">INFO@VELOCARGO.DE</span></div>
<header class="header">
  <div class="brand"><i></i>VeloCargo</div>
  <nav class="nav"><span>SERVICES ⌄</span><span>ABOUT US</span><span>CONTACT</span></nav>
  <div class="nav-cta">GET A QUOTE</div>
</header>

<section class="hero" role="img" aria-label="Photo of a cargo aircraft being loaded on an airport apron">
  <h1>Swift &amp;<br>Air Logistics</h1>
  <p>Experience the speed of air freight with advanced tracking, reliable handling and timely delivery to every destination, helping your business stay on schedule.</p>
  <div class="btn">GET A QUOTE</div>
</section>
<div class="side-tabs">
  <div><svg width="16" height="16" viewBox="0 0 16 16" fill="none" stroke="#fff"><rect x="3" y="1.5" width="10" height="13"/><path d="M5.5 5h5M5.5 8h5M5.5 11h3"/></svg>GET A QUOTE</div>
  <div><svg width="16" height="16" viewBox="0 0 16 16" fill="none" stroke="#fff"><path d="M3 2h3l1.5 3.5-2 1.3a8 8 0 0 0 3.7 3.7l1.3-2L14 10v3a1 1 0 0 1-1 1A11 11 0 0 1 2 3a1 1 0 0 1 1-1z"/></svg>CONTACT</div>
</div>

<div class="eyebrow" style="left:186px;top:712px">Who <span>we are</span></div>
<div class="h2" style="left:186px;top:730px;line-height:1.15">VeloCargo – Your<br>Logistics Partner</div>
<p class="about-text">VeloCargo is a leading freight company providing excellent transport services worldwide.</p>
<p class="about-small" style="top:888px">With a customer-first approach we ensure clear communication, accurate tracking and safe handling.</p>
<p class="about-small" style="top:926px">Trust us to handle your cargo with care.</p>
<div class="btn-outline" style="left:186px;top:971px;width:98px;height:26px">ABOUT US</div>
<div class="about-img" role="img" aria-label="Photo of stacked shipping containers at a port terminal"></div>

<div class="eyebrow" style="left:186px;top:1160px">Why <span>us</span></div>
<div class="h2" style="left:186px;top:1176px">Our services</div>
<div class="pager"><span style="font-size:16px">←</span><span>1 / 3</span><span class="next"><svg width="14" height="10" viewBox="0 0 14 10" fill="none" stroke="#fff" stroke-width="1.5"><path d="M0 5h12M8 1l4 4-4 4"/></svg></span></div>

<div class="card" style="left:186px"><div class="ic"><svg width="40" height="40" viewBox="0 0 40 40" fill="none" stroke="#999"><path d="M8 32h24M12 32V14l8-6 8 6v18M16 22h8v10h-8z"/></svg><span class="badge"></span></div><h3><b>Import</b> - Simplify your sea freight imports with VeloCargo.</h3><p>Our expert team handles documentation, customs clearance, and transport coordination for efficient imports.</p></div>
<div class="card" style="left:430px"><div class="ic"><svg width="40" height="40" viewBox="0 0 40 40" fill="none" stroke="#999"><path d="M8 32h24M12 32V14l8-6 8 6v18M16 22h8v10h-8z"/></svg><span class="badge"></span></div><h3><b>Export</b> - Efficient Sea Freight Export Services</h3><p>Our expert team handles documentation, customs clearance, and transportation coordination for seamless and efficient export operations.</p></div>
<div class="card" style="left:674px"><div class="ic"><svg width="40" height="40" viewBox="0 0 40 40" fill="none" stroke="#999"><path d="M10 8l6 22h16M14 14h14l-2 10H17"/><circle cx="18" cy="33" r="2"/><circle cx="29" cy="33" r="2"/></svg><span class="badge"></span></div><h3><b>Warehousing</b> - Secure and Reliable Warehousing Solutions</h3><p>Our expert team handles documentation, customs clearance, and transport coordination for efficient storage.</p></div>
<div class="card" style="left:918px"><div class="ic"><svg width="40" height="40" viewBox="0 0 40 40" fill="none" stroke="#999"><circle cx="20" cy="20" r="12"/><path d="M14 20h12M20 14v12"/></svg><span class="badge"></span></div><h3><b>Support</b> - Secure and Reliable Warehousing</h3><p>Our expert team handles documentation, customs clearance, and transportation coordination for seamless and efficient operations.</p></div>
<div class="card" style="left:1162px"></div>

<section class="reach">
  <div class="reach-img" role="img" aria-label="Aerial photo of a container ship and a truck at the quay"></div>
  <h2>Reach Out to Us</h2>
  <p>We're here to assist you. Contact our team for any inquiries or support you may need.</p>
  <div class="btn-outline">GET A QUOTE</div>
  <div class="phone"><svg width="22" height="22" viewBox="0 0 16 16" fill="none" stroke="#fff"><path d="M3 2h3l1.5 3.5-2 1.3a8 8 0 0 0 3.7 3.7l1.3-2L14 10v3a1 1 0 0 1-1 1A11 11 0 0 1 2 3a1 1 0 0 1 1-1z"/></svg>+49 6100 4417720</div>
  <div class="hours"><svg width="14" height="14" viewBox="0 0 14 14" fill="none" stroke="#b9c5cd"><circle cx="7" cy="7" r="6"/><path d="M7 3.5V7l2.5 1.5"/></svg><div><b>Our business hours:</b>Monday to Friday, 8:00 AM to 6:00 PM (CET)</div><div><b>We are open in:</b>7 hours and 20 minutes</div></div>
</section>

<div class="eyebrow center" style="top:2110px">Our <span>values</span></div>
<div class="h2" style="left:0;width:1200px;text-align:center;top:2126px">Our Philosophy</div>
<div class="pcard" style="left:186px;top:2214px;width:264px;height:183px"><svg width="20" height="20" viewBox="0 0 20 20" fill="none" stroke="#e2001a"><path d="M10 2l2.4 5 5.4.7-4 3.8 1 5.4L10 14.3 5.2 17l1-5.4-4-3.8 5.4-.7z"/></svg><h3>Expertise</h3><p>With years of experience in the industry, our team has the knowledge and expertise to handle all your air freight needs efficiently and effectively.</p></div>
<div class="pcard" style="left:467px;top:2214px;width:264px;height:183px"><svg width="20" height="20" viewBox="0 0 20 20" fill="none" stroke="#e2001a"><rect x="2" y="2" width="16" height="16"/><circle cx="10" cy="8" r="3"/><path d="M5 16c1-3 9-3 10 0"/></svg><h3>Customer Focus</h3><p>Your satisfaction is our top priority. We provide personalized support, responsive customer service, and transparent communication throughout the entire process.</p></div>
<div class="pcard" style="left:748px;top:2214px;width:264px;height:183px"><svg width="20" height="20" viewBox="0 0 20 20" fill="none" stroke="#e2001a"><circle cx="10" cy="10" r="8"/><path d="M2 10h16M10 2c3 3 3 13 0 16M10 2c-3 3-3 13 0 16"/></svg><h3>Global Network</h3><p>We have established a vast network of partners and agents worldwide, enabling us to provide seamless door-to-door solutions to any destination.</p></div>
<div class="pcard" style="left:186px;top:2411px;width:404px;height:163px"><svg width="20" height="20" viewBox="0 0 20 20" fill="none" stroke="#e2001a"><rect x="4" y="4" width="12" height="12"/><circle cx="4" cy="4" r="2"/><circle cx="16" cy="16" r="2"/></svg><h3>Customization</h3><p>We understand that every shipment is unique. That's why we offer tailored solutions, ensuring your cargo is handled with precision and according to your specific requirements.</p></div>
<div class="pcard" style="left:608px;top:2411px;width:404px;height:163px"><svg width="20" height="20" viewBox="0 0 20 20" fill="none" stroke="#e2001a"><circle cx="10" cy="10" r="3"/><circle cx="10" cy="10" r="7" stroke-dasharray="3 2"/></svg><h3>Reliability</h3><p>We prioritize reliability and on-time delivery. You can trust us to keep your supply chain running smoothly, with proactive communication and real-time tracking.</p></div>

<div class="eyebrow center" style="top:2762px">Our <span>values</span></div>
<div class="h2" style="left:0;width:1200px;text-align:center;top:2778px">Our Philosophy</div>
<div class="faq" style="left:186px;top:2870px;width:404px">What is sea freight and how does it work?</div>
<div class="faq" style="left:186px;top:2933px;width:404px">How long does sea freight shipping typically take?</div>
<div class="faq" style="left:186px;top:2996px;width:404px">Do you offer both full container load (FCL) and less than container load (LCL) options?</div>
<div class="faq" style="left:186px;top:3059px;width:404px">Are there any restrictions or prohibited items for sea freight shipping?</div>
<div class="faq" style="left:186px;top:3122px;width:404px">What happens if there are delays or disruptions in the sea freight transportation?</div>
<div class="faq" style="left:608px;top:2870px;width:404px">What are the advantages of choosing sea freight over other shipping methods?</div>
<div class="faq" style="left:608px;top:2933px;width:404px">What are the main factors that affect sea freight shipping costs?</div>
<div class="faq" style="left:608px;top:2996px;width:404px">What is the process for customs clearance during sea freight shipments?</div>
<div class="faq" style="left:608px;top:3059px;width:404px">How can I track the progress of my sea freight shipment?</div>
<div class="faq" style="left:608px;top:3122px;width:404px">What documentation is required for sea freight shipments, and how can I ensure compliance?</div>

<div class="eyebrow" style="left:186px;top:3296px">Who <span>trusts us</span></div>
<div class="abs" style="left:186px;top:3314px;font-size:23px;font-weight:600;color:#333">Our Partners and clients</div>
<div class="partner" style="left:186px"><i></i>Northline</div>
<div class="partner" style="left:390px">Westwing Air</div>
<div class="partner" style="left:600px">Kessler Motors</div>
<div class="partner" style="left:790px"><i style="border-radius:0"></i>Portaxa</div>

<footer class="footer">
  <div class="logo"><i></i>VeloCargo</div>
  <div class="tag">Moving Logistics Forward.<br>Your Reliable Partner</div>
  <div class="cert" role="img" aria-label="Air cargo association badge"></div>
  <div class="cert-t">Certified air cargo partner</div>
  <div class="fcol" style="left:398px;top:85px"><h4>OUR SERVICES</h4><a>AIR FREIGHT</a><a>SEA FREIGHT</a><a>LAND TRANSPORT</a><a>AIRLINE SERVICES</a></div>
  <div class="fcol" style="left:540px;top:85px"><h4>LEGAL INFORMATION</h4><a>DATA PRIVACY POLICY</a><a>IMPRINT</a></div>
  <div class="fcol" style="left:540px;top:198px"><h4>OTHER INFORMATION</h4><a>FAQ</a><a>CONTACT</a></div>
  <div class="rule"></div>
  <div class="map" role="img" aria-label="Map showing the office location"></div>
  <div class="contact"><h4>CONTACT INFORMATION</h4><b>VeloCargo GmbH</b><br>Hafenweg 12<br>60311 Frankfurt<br>Tel.: +49 6100 4417720<br>E-Mail: info@velocargo.de</div>
  <div class="rating" role="img" aria-label="Client rating badge"></div>
  <div class="btn-outline">CONTACT FORM</div>
</footer>

<div class="overlay"></div>

<div class="modal" role="dialog" aria-label="Get a Quote">
  <svg class="close" width="12" height="12" viewBox="0 0 12 12" stroke="#2b5f9e" stroke-width="1.4"><path d="M1 1l10 10M11 1L1 11"/></svg>
  <div class="eyebrow">Contact</div>
  <h2>Get a Quote</h2>
  <p class="intro">Thank you for your interest. Please fill out the fields below, and we will get back to you as soon as possible. We look forward to assisting you.</p>
  <div class="person"><div class="avatar" role="img" aria-label="Portrait of the contact person"></div><div><b>Your Contact Person</b><span>Jonas Berger</span></div></div>

  <div class="group" style="top:253px">Customer Data</div>
  <div class="label" style="left:35px;top:284px">Salutation</div>
  <div class="field" style="left:35px;top:302px;width:286px">Please Select<svg class="chev" width="8" height="6" viewBox="0 0 8 6" fill="none" stroke="#333" stroke-width="1.4"><path d="M1 1l3 3 3-3"/></svg></div>
  <div class="label" style="left:35px;top:353px">Your Name</div>
  <div class="field ph" style="left:35px;top:371px;width:286px">Your name</div>
  <div class="label" style="left:340px;top:353px">Your Company</div>
  <div class="field ph" style="left:340px;top:371px;width:287px">Your company name</div>

  <div class="group" style="top:444px">Contact</div>
  <div class="label" style="left:35px;top:476px">E-Mail</div>
  <div class="field ph" style="left:35px;top:493px;width:286px">f.e. yourmail@adress.com</div>
  <div class="label" style="left:340px;top:476px">Country</div>
  <div class="field" style="left:340px;top:493px;width:74px">DE&nbsp;&nbsp; +49<svg class="chev" width="8" height="6" viewBox="0 0 8 6" fill="none" stroke="#333" stroke-width="1.4"><path d="M1 1l3 3 3-3"/></svg></div>
  <div class="label" style="left:420px;top:476px">Phonenumber</div>
  <div class="field ph" style="left:420px;top:493px;width:207px">z.B. 941 / 941-9791</div>

  <div class="group" style="top:569px">Your message</div>
  <div class="label" style="left:35px;top:600px">Freight type (optional)</div>
  <div class="field" style="left:35px;top:618px;width:286px">Air Freight<svg class="chev" width="8" height="6" viewBox="0 0 8 6" fill="none" stroke="#333" stroke-width="1.4"><path d="M1 1l3 3 3-3"/></svg></div>
  <div class="label" style="left:35px;top:669px">Your message (optional)</div>
  <div class="field area" style="left:35px;top:686px;width:592px">Please tell us something about your project</div>

  <div class="consent"><i></i><span>Yes, I agree that my personal data provided in the contact form may be processed to find a suitable offer for my inquiry and I have read the <a>Data Privacy Policy</a>.</span></div>
  <div class="submit">SUBMIT FORM</div>
</div>

</body>
</html>
```